I need a business card for my original fine art pieces

I would like a business card design including a logo design for a new business in the art world. I am based in the Hunter Valley NSW Australia. I am a contemporary figurative, encaustic and wildlife artist. I would like to be able to upload my email and mobile number to this as well. This design should be one that I can incorporate into banners and flyers etc. Id like to incorporate one of my own images or partial image into the background or somewhere below. My initials are KD and I would like these used as a logo type. I would like the use of some colour and it to be bright and catchy. The final design should communicate artwork custom made and commissions available.

Overview: Original Fine Artworks for sale, online, art galleries etc, Custom made to order and by commission.

Target market is world wide audience and corporate world

My figurative work is painted using acrylics in a lot of natural ochre colours that reflect the Australian Outback, on canvas, linen, paper or board: My encaustic work is created in a contemporary abstract style using a blow torch and a made with a medium of 100% pure bees wax, Damar resin, mixed media and coloured pigments, applied to Birch board. My wildlife are created using coloured pencil and mixed media on a variety of paper types or board.

```html
<!DOCTYPE html>
<html lang="en">
<head>
<meta charset="utf-8">
<title>Kira Dalton – Business Card</title>
<link rel="stylesheet" href="https://fonts.googleapis.com/css2?family=Cinzel:wght@500&family=Poiret+One&family=Questrial&display=swap">
<style>
  :root {
    --page: #ffffff;
    --maroon-deep: #3e0c05;
    --maroon: #5a1709;
    --ochre: #7d6a20;
    --ochre-light: #9a8530;
    --moss: #6f7a36;
    --vermilion: #c8441f;
    --sand: #d9c59b;
    --gold: #d6ae6c;
    --ghost: rgba(160, 110, 60, 0.22);
  }
  * { margin: 0; padding: 0; box-sizing: border-box; }
  html, body {
    width: 996px; height: 1200px; overflow: hidden;
    background: var(--page);
  }
  .canvas { position: relative; width: 996px; height: 1200px; }

  .card {
    position: absolute; overflow: hidden;
    background: var(--maroon-deep);
  }
  .card--front { left: 42px; top: 59px; width: 900px; height: 514px; }
  .card--back  { left: 42px; top: 626px; width: 912px; height: 511px; }

  .card__artwork {
    position: absolute; inset: 0;
    background:
      radial-gradient(ellipse 160px 110px at 12% 22%, rgba(111,122,54,0.45), transparent 70%),
      radial-gradient(ellipse 120px 160px at 8% 60%, rgba(111,122,54,0.40), transparent 70%),
      radial-gradient(ellipse 200px 120px at 30% 85%, rgba(125,106,32,0.35), transparent 70%),
      radial-gradient(ellipse 220px 140px at 70% 30%, rgba(125,106,32,0.30), transparent 70%),
      radial-gradient(ellipse 160px 120px at 90% 80%, rgba(111,122,54,0.35), transparent 70%),
      linear-gradient(135deg, var(--maroon) 0%, var(--maroon-deep) 55%, var(--maroon) 100%);
  }

  .card__sweep { position: absolute; inset: 0; }

  .brand-mark {
    position: absolute; left: 0; width: 100%;
    display: flex; align-items: center; justify-content: center; gap: 18px;
    font-family: "Cinzel", serif; font-weight: 500; line-height: 1;
  }
  .brand-mark--front {
    top: 140px; font-size: 104px; color: var(--vermilion);
  }
  .brand-mark--back {
    top: 130px; font-size: 230px; color: var(--ghost);
  }
  .brand-mark__dot {
    width: 22px; height: 22px; border-radius: 50%;
    background: var(--vermilion);
  }

  .brand {
    position: absolute; left: 0; width: 100%; text-align: center;
  }
  .brand__name {
    top: 312px;
    font-family: "Cinzel", serif; font-weight: 500;
    font-size: 72px; line-height: 1; letter-spacing: 3px;
    color: var(--vermilion);
  }
  .brand__tagline {
    top: 391px;
    font-family: "Questrial", sans-serif;
    font-size: 30px; line-height: 1; letter-spacing: 6px;
    color: var(--sand);
  }

  .contact {
    position: absolute; left: 0; width: 100%; top: 200px;
    list-style: none; text-align: center;
    font-family: "Poiret One", sans-serif;
    font-size: 22px; line-height: 47px; letter-spacing: 0.5px;
    text-transform: uppercase; color: var(--gold);
  }
</style>
</head>
<body>
<main class="canvas">

  <section class="card card--front" aria-label="Business card front">
    <div class="card__artwork" role="img" aria-label="Painterly abstract artwork in maroon and ochre tones"></div>
    <svg class="card__sweep" width="900" height="514" viewBox="0 0 900 514" aria-hidden="true">
      <defs>
        <linearGradient id="sweepFill" x1="0" y1="0" x2="1" y2="1">
          <stop offset="0" stop-color="#9a8530"/>
          <stop offset="1" stop-color="#7a6620"/>
        </linearGradient>
      </defs>
      <path d="M801 0 C 740 250, 600 440, 374 514 L 900 514 L 900 0 Z" fill="url(#sweepFill)" opacity="0.85"/>
    </svg>

    <div class="brand-mark brand-mark--front" aria-label="KD">
      <span class="brand-mark__text">KD</span>
      <span class="brand-mark__dot" aria-hidden="true"></span>
    </div>

    <h1 class="brand brand__name">Kira Dalton</h1>
    <p class="brand brand__tagline">ORIGINAL FINE ARTWORKS</p>
  </section>

  <section class="card card--back" aria-label="Business card back">
    <div class="card__artwork" role="img" aria-label="Painterly abstract artwork in maroon and ochre tones"></div>

    <div class="brand-mark brand-mark--back" aria-hidden="true">
      <span class="brand-mark__text">KD</span>
    </div>

    <ul class="contact">
      <li class="contact__phone">T: 0455 318 472</li>
      <li class="contact__email">E: kiradalton@studiokd.com</li>
      <li class="contact__address">Harlow Avenue 22 2325 Millbrook Hunter Valley NSW</li>
    </ul>
  </section>

</main>
</body>
</html>
```